Real Estate Development requires a tri-fold corporate brochure

I need a clean, elegant, Corporate tri-fold brochure for a real estate development. Currently operation in Dubai, we plan to enter European markets and will hand out the brochures to potential, future cooperation partners. A color combination in line with our logo would be great. The overall design should communicate that we are holding numerous high-end properties in Dubai and London and our financial strength.

Target Market(s)

Europe

Industry/Entity Type

Real Estate Development

Contact Information for Business Card

Lorin Paskow, MBA
Senior Business Development Manager
Meadow Crest UAE
Cell UAE: +971 52 408 1396
Cell Austria: +43 664 317 2809
lopa@meadowcrest.example

Requirements
Must have
• Clean, corporate design, not too colorful, a few nice pictures of existing real estate properties. See the attached pdf-document for more details.
Nice to have
• Refurbished logo

```html
<!DOCTYPE html>
<html lang="en">
<head>
<meta charset="utf-8">
<title>Meadow Crest – Corporate Tri-fold Brochure</title>
<link href="https://fonts.googleapis.com/css2?family=Oxanium:wght@600&family=Montserrat:wght@400;600&display=swap" rel="stylesheet">
<style>
  :root {
    --green: #a5c83f;
    --green-dark: #93b52f;
    --white: #ffffff;
    --paper: #f7f7f5;
    --ink: #4a4a4a;
    --stage: #e9e9e9;
    --sky: #9fb4c8;
    --city: #6f7f86;
    --brick: #8a6a52;
    --lawn: #6f9a3a;
  }
  * { margin: 0; padding: 0; box-sizing: border-box; }
  html, body { width: 1200px; height: 1200px; overflow: hidden; }
  body {
    background: var(--stage);
    font-family: "Montserrat", sans-serif;
    color: var(--ink);
    display: flex; flex-direction: column; align-items: center;
    gap: 40px; padding-top: 40px;
  }
  .spread { display: flex; box-shadow: 0 6px 18px rgba(0,0,0,.15); }
  .panel {
    position: relative; width: 330px; height: 540px;
    background: var(--white); overflow: hidden;
    display: flex; flex-direction: column;
  }
  .panel + .panel { border-left: 1px solid rgba(0,0,0,.06); }
  .photo { flex: none; width: 100%; }
  .photo--fill { flex: 1 1 auto; min-height: 0; }
  .photo--terrace { background: linear-gradient(160deg, #e9e4dc 0%, var(--brick) 55%, #2d4fa0 100%); }
  .photo--skyline { height: 250px; background: linear-gradient(180deg, #cfd3d2 0%, #8e8f86 45%, #5c6a70 100%); }
  .photo--marina  { height: 240px; background: linear-gradient(180deg, #c8d6e6 0%, var(--sky) 45%, #5a8a86 85%, #3f6e6a 100%); }
  .photo--london  { height: 230px; background: linear-gradient(180deg, #c7d3e0 0%, var(--city) 60%, #47535a 100%); }
  .photo--house   { background: linear-gradient(180deg, #b9c7a4 0%, #9a8b74 45%, var(--lawn) 80%, #5b8430 100%); }

  .green-block { flex: none; background: var(--green); color: var(--white); padding: 24px 26px 22px; }
  .white-block { padding: 26px; }
  .title {
    font-family: "Oxanium", sans-serif; font-weight: 600;
    text-transform: uppercase; line-height: 1.02; letter-spacing: .5px;
  }
  .title--light { color: var(--white); font-size: 26px; margin-bottom: 12px; }
  .title--green { color: var(--green); font-size: 28px; margin-bottom: 14px; }
  .body-copy { font-size: 10.5px; line-height: 1.55; text-align: justify; }
  .body-copy + .body-copy { margin-top: 8px; }

  .cover .curve { display: block; width: 100%; height: 40px; margin-top: -40px; }
  .cover .brand-area {
    flex: 1; display: flex; align-items: center; justify-content: center; gap: 10px;
  }
  .brand-mark { width: 14px; height: 14px; background: var(--green); }
  .brand-name { font-family: "Montserrat", sans-serif; font-weight: 600; font-size: 24px; color: var(--ink); }
  .brand-tag { font-family: "Montserrat", sans-serif; font-weight: 400; font-size: 10px; color: var(--ink); letter-spacing: .5px; margin-top: 4px; }
  .cover .tagline-area { position: relative; flex: none; height: 150px; background: var(--green); }
  .cover .tagline-area svg { position: absolute; top: -30px; left: 0; width: 100%; height: 31px; }
  .cover .tagline {
    position: absolute; left: 0; right: 0; top: 42px; text-align: center;
    font-family: "Oxanium", sans-serif; font-weight: 600; font-size: 34px;
    line-height: 1; color: var(--white); text-transform: uppercase;
  }
</style>
</head>
<body>

  <section class="spread spread--outside">
    <article class="panel about">
      <div class="green-block">
        <h2 class="title title--light">About</h2>
        <p class="body-copy">From its inception, Meadow Crest Co. Ltd capitalized on profitable market niches acquiring, developing and managing investment grade real estate properties in the United Arab Emirates such as the Harbor Spire, the world's tallest tower, and Europe including but not limited to Germany, France, Cyprus and the UK. Today, with its capital resources and expertise, Meadow Crest is well positioned for continued success in the real estate market, not at last because it invests without the constraints of a traditional fund-based business model – Meadow Crest Co. Ltd. solely uses own capital to fund investments.</p>
      </div>
      <div class="photo photo--fill photo--terrace" role="img" aria-label="Photo of a row of white-trimmed brick terraced houses under a blue sky"></div>
    </article>

    <article class="panel selected">
      <div class="photo photo--skyline" role="img" aria-label="Aerial photo of a dense city skyline with highways and towers"></div>
      <div class="white-block">
        <h2 class="title title--green">Selected Properties</h2>
        <p class="body-copy">A Sampling of Property Acquisitions made by Meadow Crest Company Ltd. Please contact us for any further questions in regards to our acquisition profile and any other further information. We are looking very much forward to hearing back from you and would be pleased to receive a brief overview/listing of properties available soon.</p>
      </div>
    </article>

    <article class="panel cover">
      <div class="photo photo--marina" role="img" aria-label="Photo of waterfront skyscrapers and a yacht marina"></div>
      <svg class="curve" viewBox="0 0 330 40" preserveAspectRatio="none" aria-hidden="true"><path d="M0 40 Q165 0 330 22 L330 40 Z" fill="#ffffff"/></svg>
      <div class="brand-area">
        <span class="brand-mark"></span>
        <div>
          <div class="brand-name">Meadow Crest</div>
          <div class="brand-tag">Company LTD</div>
        </div>
      </div>
      <div class="tagline-area">
        <svg viewBox="0 0 330 31" preserveAspectRatio="none" aria-hidden="true"><path d="M0 31 L0 18 Q165 -8 330 10 L330 31 Z" fill="#a5c83f"/></svg>
        <p class="tagline">Real-Estate<br>Competence</p>
      </div>
    </article>
  </section>

  <section class="spread spread--inside">
    <article class="panel acquisition">
      <div class="photo photo--london" role="img" aria-label="Aerial photo of a riverside city centre with office towers"></div>
      <div class="white-block">
        <h2 class="title title--green">Acquisition Profile</h2>
        <p class="body-copy">Our properties span a broad range of sectors including hospitality, leisure, residential and commercial. This includes both development and completed properties. We seek underperforming assets where we can add value through repositioning, redeployment, or refurbishment, in mid and long term real estate opportunities with a potential for capital gain and solid rental income.</p>
      </div>
    </article>

    <article class="panel diversification">
      <div class="green-block">
        <h2 class="title title--light">Further Diversification<br>EU &amp; Approach</h2>
        <p class="body-copy">We are currently exploring possible opportunities and cooperations in context with our plans of further diversifying our real-estate portfolio i.e. the intention to further invest in opportunities in European Union Member Countries.</p>
        <p class="body-copy">Acquistion Approach: By identifying opportunities and adding real value, we have consistently produced industry-leading returns across all asset classes. The end goal is to capitalize on market inefficiencies, creating value through strategic acquisitions, effective management and well-timed divestitures.</p>
      </div>
      <div class="photo photo--fill photo--house" role="img" aria-label="Photo of a large detached family home with a landscaped lawn"></div>
    </article>
  </section>

</body>
</html>
```